PIKEmoor box Graphic design on existing box dye cut.

we are a flooring company and we are making a sample box. the logo and information that need to be on the box is already established. we just need someone to lay it out on the box "DYE_CUT" . PLEASE CHANGE DASHES ON LOOK TOUCH PICK TO DOTS AND REMOVE THE EXCLAMATION POINT ALSO, please give me a lighter version of the logo...it appears a bit dark on the box. perhaps lighten a bit. .so we need to work with someone who understands how to work with a box dye cut. We want to wrap the logo around the entire 4 sides of the box and leave the top and bottom a black color. The inside of the box will have a similar photo with bullet points (be creative how to include them). I have enclosed a picture of this how it should read. Also, the large inside flap will have a specification sheet. I have included photos of this sheet for your reference… all spec information needs to be included as written. We need to include a QR code on this inside flap which will later allow architects to download the spec.The very front cover that we submitted with the PIKEMOOR look touch pick…I would like a few reeditions of the font on this as I am not completely sold on the font. I am including pictures of how it should look, from a cut and paste model I made.

Target Market(s)

architects and designers

Industry/Entity Type

Architecture

Colors
474747

Requirements
Must have
• Graphic designer MUST know how to work with dye cuts provided and scale artwork to work on dye cut sizes provided. must look professional and elegant this is for architects and designers
Nice to have
• box must look good from all sides . short and long sides. pikemoor photo needs to be on all 4 sides...

```html
<!DOCTYPE html>
<html lang="en">
<head>
<meta charset="utf-8">
<title>PIKEMOOR sample box die line</title>
<link href="https://fonts.googleapis.com/css2?family=Montserrat:wght@500;700;800&family=Arimo:wght@400;700&display=swap" rel="stylesheet">
<style>
  :root {
    --paper: #ffffff;
    --ink: #000000;
    --flap: #ededed;
    --flap-edge: #555555;
    --bleed: #e0141b;
    --dimension: #1010d8;
    --brand-grey: #474747;
  }
  html, body { margin: 0; padding: 0; overflow: hidden; background: var(--paper); }
  .dieline { display: block; width: 1200px; height: 1000px; }
  .flap { fill: var(--flap); stroke: var(--flap-edge); stroke-width: 1; }
  .solid { fill: var(--ink); }
  .wood { fill: url(#woodGrain); }
  .bleed-line { stroke: var(--bleed); stroke-width: 1.2; }
  .slot { fill: var(--flap); stroke: var(--flap-edge); stroke-width: .8; }
  .brand { font-family: "Montserrat", sans-serif; font-weight: 800; fill: var(--ink); }
  .brand-tag { font-family: "Montserrat", sans-serif; font-weight: 700; fill: var(--ink); }
  .brand.on-black, .brand-tag.on-black { fill: var(--paper); }
  .bullets { font-family: "Arimo", sans-serif; font-weight: 700; font-size: 6.3px; fill: var(--paper); }
  .spec-sheet { fill: var(--paper); }
  .spec { font-family: "Arimo", sans-serif; font-size: 3.7px; fill: var(--ink); }
  .spec-head { font-family: "Arimo", sans-serif; font-size: 4px; font-weight: 700; fill: var(--ink); }
  .dim-line { stroke: var(--dimension); stroke-width: 1.2; fill: none; }
  .dim-label { font-family: "Arimo", sans-serif; font-size: 15px; fill: var(--dimension); }
  .dim-total { font-family: "Arimo", sans-serif; font-size: 17px; font-weight: 700; fill: var(--dimension); }
  .frac { font-size: 10px; }
</style>
</head>
<body>
<svg class="dieline" viewBox="0 0 1200 1000" xmlns="http://www.w3.org/2000/svg">
  <defs>
    <linearGradient id="woodGrain" x1="0" y1="0" x2="1" y2="0">
      <stop offset="0" stop-color="#8c8c8c"/>
      <stop offset=".2" stop-color="#c4c4c4"/>
      <stop offset=".4" stop-color="#a2a2a2"/>
      <stop offset=".6" stop-color="#cfcfcf"/>
      <stop offset=".8" stop-color="#9c9c9c"/>
      <stop offset="1" stop-color="#b8b8b8"/>
    </linearGradient>
    <marker id="arrow" viewBox="0 0 10 10" refX="9" refY="5" markerWidth="8" markerHeight="8" orient="auto-start-reverse">
      <path d="M0 0 L10 5 L0 10" fill="none" stroke="#1010d8" stroke-width="1.5"/>
    </marker>
  </defs>

  <!-- lid flap -->
  <g class="lid">
    <path class="solid" d="M520 46 L685 46 Q740 46 762 60 Q786 84 786 114 Q786 138 770 145 Q740 151 690 155 L513 155 Q463 151 433 145 Q417 138 417 114 Q417 84 441 60 Q463 46 520 46 Z"/>
    <rect class="wood" x="518" y="46" width="168" height="109" role="img" aria-label="Grey weathered wood plank photo with a curious pet peeking through"/>
    <line class="bleed-line" x1="518" y1="46" x2="518" y2="155"/>
    <line class="bleed-line" x1="686" y1="46" x2="686" y2="155"/>
    <text class="brand" x="531" y="70" font-size="14" textLength="84" lengthAdjust="spacingAndGlyphs">PIKEMOOR</text>
    <text class="brand-tag" x="532" y="80" font-size="7" textLength="84" lengthAdjust="spacing">LOOK · TOUCH · PICK</text>
    <g class="bullets">
      <text x="580" y="92">ULTIMATE DESIGN FLEXIBILITY</text>
      <text x="580" y="102">• Multiple widths, grades, finishes</text>
      <text x="580" y="112">• 50+ Colors</text>
      <text x="580" y="122">• ASTM E84 Class B rated for use on walls</text>
      <text x="580" y="132">• 3-4 week lead time for stock</text>
      <text x="580" y="142">• Meets most commercial needs</text>
    </g>
  </g>

  <!-- specification flap -->
  <g class="spec-flap">
    <rect class="solid" x="513" y="155" width="177" height="216"/>
    <rect class="spec-sheet" x="520" y="161" width="163" height="204"/>
    <rect x="523" y="164" width="157" height="198" fill="none" stroke="#000" stroke-width=".6"/>
    <g class="spec">
      <text x="537" y="177">Species :</text><text x="580" y="177">Balanced French White Oak</text>
      <text x="537" y="184">Construction:</text><text x="580" y="184">Engineered hardwood</text>
      <text x="537" y="191">Plank Sizes :</text><text x="580" y="191">5" or 7" wide x 5/8" thick x 23" - 86" Random lengths</text>
      <text x="580" y="196">7" or 10" wide x 3/4" thick x 23" - 120" Random lengths</text>
      <text x="580" y="201">14" wide x 3/4" thick x Random lengths to 15'</text>
      <text x="537" y="208">Patterns Available:</text><text x="580" y="208">Herringbone     5" x 5/8" x 25" or 7" x 5/8" x 28"</text>
      <text x="580" y="213">Chevron            5" x 5/8" x 25"</text>
      <text x="537" y="220">Grade :</text><text x="580" y="220">Character, Plain Sawn</text>
      <text x="580" y="225">Option for Select, Rift &amp; Quartered</text>
      <text x="537" y="230">Texture:</text><text x="580" y="230">Wirebrush</text>
      <text x="537" y="240">Finish:</text><text x="580" y="240">UV oil</text>
      <text x="537" y="247">Wear Layer :</text><text x="580" y="247">5/8" thick planks have a 3mm wear layer</text>
      <text x="580" y="252">3/4" thick planks have a 5mm wear layer</text>
      <text x="537" y="259">US Fire Test Ratings:</text><text x="580" y="259">ASTM E84 Class B rated for use on walls</text>
      <text x="537" y="268">Certifications:</text><text x="580" y="268">SoundFloor and ForestMark Certified</text>
      <text x="537" y="276">Structure warranty:</text><text x="580" y="276">Lifetime-see warranty for details</text>
      <text x="537" y="282">Installation :</text><text x="580" y="282">Glue Down, Nail &amp; Staple</text>
      <text x="537" y="288">Suitable for use over radiant heat. Matching stair nosings and other</text>
      <text x="537" y="293">accessories available</text>
      <text x="537" y="299">Expect to see variations in color, grain, character including knots and black</text>
      <text x="537" y="304">fill. Wood color and tone to vary from plank to and sample to sample.</text>
      <text x="537" y="310">*Confirm with your local code requirements</text>
    </g>
    <text class="spec-head" x="601" y="319" text-anchor="middle" textLength="146" lengthAdjust="spacingAndGlyphs">FABRICATED SQUARE EDGE STAIR NOSE, TREADS &amp; TRANSITIONS</text>
    <text class="spec-head" x="601" y="325" text-anchor="middle">THAT MATCH YOUR WOOD FLOOR</text>
    <rect x="538" y="331" width="85" height="22" fill="#f4f4f4" stroke="#000" stroke-width=".5" role="img" aria-label="Stair nose profile drawing with dimensions"/>
    <rect x="630" y="331" width="46" height="18" fill="#f4f4f4" stroke="#000" stroke-width=".5" role="img" aria-label="Reducer transition profile drawing"/>
    <text class="spec" x="653" y="356" text-anchor="middle">Reducer 78" in Length</text>
  </g>

  <!-- upper row: back panel and dust flaps -->
  <rect class="flap" x="413" y="376" width="105" height="108"/>
  <rect class="flap" x="686" y="376" width="109" height="108"/>
  <g class="back-panel">
    <rect class="wood" x="518" y="371" width="168" height="113" role="img" aria-label="Grey weathered wood plank photo with a curious pet peeking through"/>
    <g transform="rotate(180 602 440)">
      <text class="brand" x="602" y="470" font-size="22" text-anchor="middle" textLength="134" lengthAdjust="spacingAndGlyphs">PIKEMOOR</text>
      <text class="brand-tag" x="602" y="483" font-size="10" text-anchor="middle" textLength="134" lengthAdjust="spacing">LOOK · TOUCH · PICK</text>
    </g>
  </g>

  <!-- middle row -->
  <path class="flap" d="M400 484 L293 484 L293 548 L300 556 L300 626 L293 634 L293 697 L400 697 Z"/>
  <path class="flap" d="M800 484 L917 484 L917 548 L910 556 L910 626 L917 634 L917 697 L800 697 Z"/>
  <g class="left-panel">
    <rect class="wood" x="400" y="484" width="118" height="213" role="img" aria-label="Grey weathered wood plank photo with a curious pet peeking through"/>
    <g transform="translate(518 484) rotate(90)">
      <text class="brand" x="24" y="30" font-size="29" textLength="166" lengthAdjust="spacingAndGlyphs">PIKEMOOR</text>
      <text class="brand-tag" x="26" y="46" font-size="12" textLength="162" lengthAdjust="spacing">LOOK · TOUCH · PICK</text>
    </g>
  </g>
  <g class="right-panel">
    <rect class="wood" x="686" y="484" width="114" height="213" role="img" aria-label="Grey weathered wood plank photo with a curious pet peeking through"/>
    <g transform="translate(686 697) rotate(-90)">
      <text class="brand" x="22" y="46" font-size="29" textLength="166" lengthAdjust="spacingAndGlyphs">PIKEMOOR</text>
      <text class="brand-tag" x="24" y="60" font-size="12" textLength="162" lengthAdjust="spacing">LOOK · TOUCH · PICK</text>
    </g>
  </g>
  <rect class="solid" x="518" y="484" width="168" height="213"/>
  <rect class="slot" x="513" y="553" width="10" height="74" rx="5"/>
  <rect class="slot" x="681" y="553" width="10" height="74" rx="5"/>
  <rect class="slot" x="540" y="691" width="26" height="6" rx="3"/>
  <rect class="slot" x="590" y="688" width="26" height="9" rx="3"/>
  <rect class="slot" x="646" y="691" width="26" height="6" rx="3"/>
  <g class="bleed-lines">
    <line class="bleed-line" x1="400" y1="484" x2="400" y2="697"/>
    <line class="bleed-line" x1="800" y1="484" x2="800" y2="697"/>
    <line class="bleed-line" x1="518" y1="371" x2="518" y2="484"/>
    <line class="bleed-line" x1="686" y1="371" x2="686" y2="484"/>
    <line class="bleed-line" x1="518" y1="697" x2="518" y2="805"/>
    <line class="bleed-line" x1="686" y1="697" x2="686" y2="805"/>
  </g>

  <!-- lower row: front panel and dust flaps -->
  <rect class="flap" x="413" y="697" width="105" height="108"/>
  <rect class="flap" x="686" y="697" width="109" height="108"/>
  <g class="front-panel">
    <rect class="wood" x="518" y="697" width="168" height="108" role="img" aria-label="Grey weathered wood plank photo with a curious pet peeking through"/>
    <text class="brand" x="602" y="728" font-size="22" text-anchor="middle" textLength="134" lengthAdjust="spacingAndGlyphs">PIKEMOOR</text>
    <text class="brand-tag" x="602" y="741" font-size="10" text-anchor="middle" textLength="134" lengthAdjust="spacing">LOOK · TOUCH · PICK</text>
  </g>

  <!-- tuck flap -->
  <g class="tuck-flap">
    <path class="solid" d="M524 805 L680 805 L680 905 L674 912 L616 912 L612 906 L592 906 L588 912 L530 912 L524 905 Z"/>
    <rect x="590" y="906" width="24" height="8" fill="#e0141b"/>
    <text class="brand on-black" x="602" y="861" font-size="16" text-anchor="middle" textLength="100" lengthAdjust="spacingAndGlyphs">PIKEMOOR</text>
    <text class="brand-tag on-black" x="602" y="873" font-size="8" text-anchor="middle" textLength="106" lengthAdjust="spacing">LOOK · TOUCH · PICK</text>
  </g>

  <!-- dimensions -->
  <line class="dim-line" x1="263" y1="48" x2="263" y2="928" marker-start="url(#arrow)" marker-end="url(#arrow)"/>
  <line class="dim-line" x1="292" y1="967" x2="916" y2="967" marker-start="url(#arrow)" marker-end="url(#arrow)"/>
  <text class="dim-total" transform="translate(273 515) rotate(-90)">42<tspan class="frac" dy="-6">3</tspan><tspan class="frac" dy="6">/16</tspan></text>
  <text class="dim-total" x="586" y="981">29<tspan class="frac" dy="-6">7</tspan><tspan class="frac" dy="6">/8</tspan></text>
  <g class="dim-label">
    <text transform="translate(398 118) rotate(-90)">5<tspan class="frac" dy="-6">3</tspan><tspan class="frac" dy="6">/16</tspan></text>
    <text transform="translate(500 285) rotate(-90)">10<tspan class="frac" dy="-6">3</tspan><tspan class="frac" dy="6">/8</tspan></text>
    <text transform="translate(467 352) rotate(-90)">5<tspan class="frac" dy="-6">1</tspan><tspan class="frac" dy="6">/8</tspan></text>
    <text transform="translate(752 352) rotate(-90)">5<tspan class="frac" dy="-6">1</tspan><tspan class="frac" dy="6">/8</tspan></text>
    <text transform="translate(340 474) rotate(-90)">5<tspan class="frac" dy="-6">1</tspan><tspan class="frac" dy="6">/16</tspan></text>
    <text transform="translate(826 442) rotate(-90)">5<tspan class="frac" dy="-6">1</tspan><tspan class="frac" dy="6">/4</tspan></text>
    <text transform="translate(882 474) rotate(-90)">5<tspan class="frac" dy="-6">1</tspan><tspan class="frac" dy="6">/16</tspan></text>
    <text transform="translate(950 640) rotate(-90)">9<tspan class="frac" dy="-6">15</tspan><tspan class="frac" dy="6">/16</tspan></text>
    <text transform="translate(392 770) rotate(-90)">4<tspan class="frac" dy="-6">15</tspan><tspan class="frac" dy="6">/16</tspan></text>
    <text transform="translate(512 872) rotate(-90)">4<tspan class="frac" dy="-6">7</tspan><tspan class="frac" dy="6">/8</tspan></text>
    <text x="595" y="953">7<tspan class="frac" dy="-6">1</tspan><tspan class="frac" dy="6">/2</tspan></text>
  </g>
</svg>
</body>
</html>
```